Business card design needed

New company based in Brisbane, Australia. Brindle Systems. The business is focused on the delivery of network architecture design and deployment. We will provide both services and the sale of the necessary equipment to deliver the service. Cloud computing is an important element of our focus as this is an emerging market for enterprises in Queensland. Our target marketplace is medium to large corporations with complex infrastructure requirements. IT Management and above will be the typical entry point for us into these accounts. We would like to see the use of various shade of green, design should be clutter free and impress stability, trust and growth.
Updates
Hey Everyone
Just we let you all know we have changed this project to 'committed' payment status.
Looking forward to seeing the designs! Thanks for your efforts.
Best Regards
Marcus
Industry/Entity Type
Architecture
Contact Information for Business Card
Brindle Systems, Marcus Doyle, Sales Director, Level 14 Harlow Tower, 58 Penfold Street, Brisbane QLD 4000, Ph +61 7 3904 2267, M +61 4 4926 1573, E marcus.doyle@brindlesystems-example.com.au
Look and feel
Each slider illustrates characteristics of the customer's brand and the style your logo design should communicate.

```html
<!DOCTYPE html>
<html lang="en">
<head>
<meta charset="utf-8">
<title>Brindle Systems – Business Card Concepts</title>
<link rel="stylesheet" href="https://fonts.googleapis.com/css2?family=Arimo:wght@400;700&display=swap">
<style>
  :root {
    --page: #ffffff;
    --card-green: #2a5200;
    --brand-green: #1f7a0a;
    --rule-grey: #454545;
    --edge: #222222;
    --text-light: #ffffff;
  }
  * { box-sizing: border-box; margin: 0; padding: 0; }
  html, body { width: 1200px; height: 750px; overflow: hidden; background: var(--page); }
  body { font-family: "Arimo", Arial, sans-serif; }
  .stage { position: relative; width: 1200px; height: 750px; }

  .card {
    position: absolute;
    width: 541px;
    height: 317px;
    border: 1.5px solid var(--edge);
    overflow: hidden;
    background: var(--page);
  }
  .card--side { left: 38px; top: 46px; }
  .card--stacked { left: 623px; top: 46px; }
  .card--back { left: 342px; top: 396px; background: var(--card-green); }

  .brand {
    position: absolute;
    display: flex;
    flex-direction: column;
    align-items: center;
    gap: 14px;
    font-weight: 700;
    color: var(--brand-green);
    text-align: center;
    line-height: 1.25;
  }
  .brand__mark { width: 22px; height: 22px; background: currentColor; }

  .green-panel { position: absolute; background: var(--card-green); color: var(--text-light); }
  .grey-rule { position: absolute; background: var(--rule-grey); }

  .person { position: absolute; color: var(--text-light); }
  .person__name { font-size: 27px; line-height: 1.2; }
  .person__title { font-size: 21px; line-height: 1.25; }

  .contact {
    position: absolute;
    border-left: 1.5px solid var(--rule-grey);
    padding-left: 12px;
    color: var(--text-light);
    font-size: 16.5px;
    line-height: 22.5px;
    white-space: nowrap;
  }
  .contact__label { display: inline-block; width: 26px; }

  .email { position: absolute; color: var(--text-light); font-size: 13.5px; white-space: nowrap; }

  /* side layout */
  .card--side .white-panel { position: absolute; left: 0; top: 0; width: 202px; height: 100%; }
  .card--side .brand { left: 0; top: 130px; width: 202px; font-size: 21px; }
  .card--side .grey-rule { left: 202px; top: 0; width: 9px; height: 100%; }
  .card--side .green-panel { left: 211px; top: 0; right: 0; bottom: 0; }
  .card--side .person { left: 232px; top: 13px; }
  .card--side .contact { left: 338px; top: 164px; }
  .card--side .email { left: 220px; top: 286px; font-size: 12.5px; }

  /* stacked layout */
  .card--stacked .brand { left: 0; right: 0; top: 28px; flex-direction: row; justify-content: center; font-size: 22px; }
  .card--stacked .grey-rule { left: 0; top: 129px; width: 100%; height: 9px; }
  .card--stacked .green-panel { left: 0; top: 143px; right: 0; bottom: 0; }
  .card--stacked .person { left: 15px; top: 159px; }
  .card--stacked .contact { left: 338px; top: 178px; }
  .card--stacked .email { left: 60px; top: 287px; font-size: 14px; }

  /* back */
  .card--back .brand { left: 0; right: 0; top: 130px; color: var(--text-light); font-size: 24px; }
</style>
</head>
<body>
<main class="stage">

  <section class="card card--side" aria-label="Front, side panel layout">
    <div class="white-panel"></div>
    <div class="brand"><span class="brand__mark"></span><span>Brindle<br>Systems</span></div>
    <div class="grey-rule"></div>
    <div class="green-panel"></div>
    <div class="person">
      <p class="person__name">Marcus Doyle</p>
      <p class="person__title">Sales Director</p>
    </div>
    <address class="contact" style="font-style:normal">
      Level 14 Harlow Tower<br>
      58 Penfold Street<br>
      Brisbane QLD 4000<br>
      <span class="contact__label">Ph</span> +61 7 3904 2267<br>
      <span class="contact__label">M</span> +61 4 4926 1573
    </address>
    <p class="email">marcus.doyle@brindlesystems-example.com.au</p>
  </section>

  <section class="card card--stacked" aria-label="Front, stacked layout">
    <div class="brand"><span class="brand__mark"></span><span>Brindle Systems</span></div>
    <div class="grey-rule"></div>
    <div class="green-panel"></div>
    <div class="person">
      <p class="person__name">Marcus Doyle</p>
      <p class="person__title">Sales Director</p>
    </div>
    <address class="contact" style="font-style:normal">
      Level 14 Harlow Tower<br>
      58 Penfold Street<br>
      Brisbane QLD 4000<br>
      <span class="contact__label">Ph</span> +61 7 3904 2267<br>
      <span class="contact__label">M</span> +61 4 4926 1573
    </address>
    <p class="email">marcus.doyle@brindlesystems-example.com.au</p>
  </section>

  <section class="card card--back" aria-label="Card back">
    <div class="brand"><span class="brand__mark"></span><span>Brindle Systems</span></div>
  </section>

</main>
</body>
</html>
```